Cool blackchain based app company needs a website :)

pillcheckbay.net

Kinda says it all!! This is an app which sits on your smartfone / tablet. You scan a QR code from a medicinal product and our app will verify if the product you have is genuine. It's simple, It's free.

The design could be very modern and simple. It should show in graphical form how the app works and have FAQ's etc.

pillcheckbay.net is designed specifically to allow consumers verify that the medical products which they have purchased are genuine.

Detailed brief with content attached. Logo in high res and QR code attached.

Full website required.
Updates

Target Market(s)

Pharmaceutical

Industry/Entity Type

Pharmaceutical

Coding

Coded - Design and coding required

Number of Pages Required

3 page

Colors

Designer to choose colors to be used in the design.

Requirements
Must have
• Strong visuals - very simple navigation - 3 pages
Nice to have
• Animation of the process
Should not have
• Jargon!

```html
<!DOCTYPE html>
<html lang="en">
<head>
<meta charset="utf-8">
<title>FAQ – pillcheckbay.net</title>
<link rel="stylesheet" href="https://fonts.googleapis.com/css2?family=Montserrat:wght@300;400;500;600;700&display=swap">
<style>
  :root {
    --brand-blue: #1f6bb0;
    --brand-navy: #1b4a86;
    --brand-green: #3f9a35;
    --accent-green: #7cbf2f;
    --text-body: #555555;
    --text-nav: #444444;
    --text-question: #9a9a9a;
    --row-tint: #f7f7f7;
    --rule: #cfcfcf;
    --chevron: #444444;
    --page-bg: #ffffff;
  }
  * { box-sizing: border-box; margin: 0; padding: 0; }
  html, body {
    width: 1200px; height: 1053px; overflow: hidden;
    background: var(--page-bg);
    font-family: "Montserrat", Arial, sans-serif;
  }
  .page { position: relative; width: 1200px; height: 1053px; }

  /* Header */
  .site-header { position: absolute; top: 0; left: 0; width: 1200px; height: 140px; }
  .main-nav, .footer-nav { display: flex; align-items: center; font-size: 10.5px; color: var(--text-nav); }
  .main-nav { position: absolute; left: 173px; top: 108px; }
  .main-nav a, .footer-nav a { color: inherit; text-decoration: none; }
  .main-nav .sep, .footer-nav .sep { margin: 0 14px; font-size: 9px; }
  .main-nav .is-current { color: var(--brand-blue); font-weight: 700; }

  .brand { position: absolute; left: 0; width: 1200px; display: flex; flex-direction: column; align-items: center; }
  .brand-mark { border-radius: 50%; background: var(--brand-green); }
  .brand-name { font-weight: 700; color: var(--brand-navy); letter-spacing: 0.2px; }
  .brand--header { top: 24px; }
  .brand--header .brand-mark { width: 72px; height: 72px; }
  .brand--header .brand-name { font-size: 17px; margin-top: 6px; }

  .contact { position: absolute; right: 173px; top: 107px; display: flex; align-items: center; color: var(--brand-blue); font-size: 9.5px; font-weight: 700; }
  .contact .phone-icon { margin-right: 5px; }
  .contact .sep { margin: 0 10px; color: var(--brand-navy); font-weight: 400; font-size: 12px; }

  /* FAQ */
  .page-title { position: absolute; top: 166px; width: 1200px; text-align: center; font-size: 27px; font-weight: 700; color: var(--brand-blue); }
  .faq { position: absolute; left: 173px; top: 230px; width: 854px; }
  .faq-open { position: relative; height: 180px; }
  .faq-open h2 { text-align: center; font-size: 17.5px; font-weight: 600; color: var(--brand-blue); padding-left: 12px; }
  .faq-open .chevron { position: absolute; right: 13px; top: 28px; }
  .answer { width: 700px; margin: 10px auto 0; text-align: center; font-size: 10.8px; line-height: 14.4px; font-weight: 300; color: var(--text-body); }
  .answer p + p { margin-top: 14.4px; }

  .faq-list { list-style: none; border-top: 1px solid var(--rule); }
  .faq-item { position: relative; height: 48px; border-bottom: 1px solid var(--rule); display: flex; align-items: center; justify-content: center; }
  .faq-item:nth-child(odd) { background: var(--row-tint); }
  .faq-item span { font-size: 11.5px; font-weight: 600; color: var(--text-question); padding-left: 12px; }
  .faq-item .chevron { position: absolute; right: 13px; top: 20px; }

  /* Footer */
  .site-footer { position: absolute; top: 828px; left: 0; width: 1200px; }
  .brand--footer { position: static; }
  .brand--footer .brand-mark { width: 96px; height: 96px; }
  .brand--footer .brand-name { font-size: 24px; margin-top: 10px; }
  .footer-nav { justify-content: center; margin-top: 16px; }
  .legal { text-align: center; margin-top: 12px; font-size: 10px; color: var(--text-nav); }
  .legal .sep { margin: 0 10px; }
  .legal .credit { color: var(--accent-green); font-weight: 600; }
</style>
</head>
<body>
<div class="page">
  <header class="site-header">
    <nav class="main-nav">
      <a href="#">Home</a><span class="sep">I</span>
      <a href="#" class="is-current">FAQ</a><span class="sep">I</span>
      <a href="#">About Us</a>
    </nav>
    <div class="brand brand--header">
      <div class="brand-mark"></div>
      <div class="brand-name">pillcheckbay.net</div>
    </div>
    <div class="contact">
      <svg class="phone-icon" width="7" height="14" viewBox="0 0 7 14"><path d="M6 1 Q1 1 1 7 Q1 13 6 13 L6 10.5 Q3.5 10.5 3.5 7 Q3.5 3.5 6 3.5 Z" fill="var(--brand-blue)"/></svg>
      <span>+353 87 555 0142</span>
      <span class="sep">|</span>
      <svg width="17" height="12" viewBox="0 0 17 12"><rect x="0" y="0" width="17" height="12" fill="var(--brand-blue)"/><polyline points="1,1 8.5,7 16,1" fill="none" stroke="#fff" stroke-width="1.2"/><line x1="1" y1="11" x2="6.5" y2="5.5" stroke="#fff" stroke-width="1"/><line x1="16" y1="11" x2="10.5" y2="5.5" stroke="#fff" stroke-width="1"/></svg>
    </div>
  </header>

  <h1 class="page-title">FAQ</h1>

  <section class="faq">
    <div class="faq-open">
      <h2>How does it work?</h2>
      <svg class="chevron" width="16" height="10" viewBox="0 0 16 10"><polyline points="1,9 8,2 15,9" fill="none" stroke="var(--brand-blue)" stroke-width="2"/></svg>
      <div class="answer">
        <p>Each time a pharmaceutical company produces medicine, they communicate with our Blockchain database and request a unique QR code from us.&nbsp; This unique QR code is printed on the foil/packaging for the medicine.</p>
        <p>When you receive your medicine, simply scan the QR code with your phone or tablet using your pillcheckbay app.&nbsp; The app will decrypt the QR code, verify its digital signature and will check the code against the Blockchain database.</p>
        <p>If it is a valid code then the product details will be displayed in the app on your device.&nbsp; If the code fails then you will be advised that this product is not genuine and should be returned.</p>
      </div>
    </div>
    <ul class="faq-list">
      <li class="faq-item"><span>A unique code for every packet of medicine??&nbsp; Surely this is impossible??</span><svg class="chevron" width="16" height="10" viewBox="0 0 16 10"><polyline points="1,1 8,8 15,1" fill="none" stroke="var(--chevron)" stroke-width="2"/></svg></li>
      <li class="faq-item"><span>So, will pillcheckbay keep a log of the medicines I take???</span><svg class="chevron" width="16" height="10" viewBox="0 0 16 10"><polyline points="1,1 8,8 15,1" fill="none" stroke="var(--chevron)" stroke-width="2"/></svg></li>
      <li class="faq-item"><span>What’s to stop a fraudster creating their own QR codes??</span><svg class="chevron" width="16" height="10" viewBox="0 0 16 10"><polyline points="1,1 8,8 15,1" fill="none" stroke="var(--chevron)" stroke-width="2"/></svg></li>
      <li class="faq-item"><span>How much does this cost me??</span><svg class="chevron" width="16" height="10" viewBox="0 0 16 10"><polyline points="1,1 8,8 15,1" fill="none" stroke="var(--chevron)" stroke-width="2"/></svg></li>
      <li class="faq-item"><span>Will I be hounded by ads??</span><svg class="chevron" width="16" height="10" viewBox="0 0 16 10"><polyline points="1,1 8,8 15,1" fill="none" stroke="var(--chevron)" stroke-width="2"/></svg></li>
      <li class="faq-item"><span>Will you resell any of my information??</span><svg class="chevron" width="16" height="10" viewBox="0 0 16 10"><polyline points="1,1 8,8 15,1" fill="none" stroke="var(--chevron)" stroke-width="2"/></svg></li>
      <li class="faq-item"><span>Who pays for this then?</span><svg class="chevron" width="16" height="10" viewBox="0 0 16 10"><polyline points="1,1 8,8 15,1" fill="none" stroke="var(--chevron)" stroke-width="2"/></svg></li>
    </ul>
  </section>

  <footer class="site-footer">
    <div class="brand brand--footer">
      <div class="brand-mark"></div>
      <div class="brand-name">pillcheckbay.net</div>
    </div>
    <nav class="footer-nav">
      <a href="#">Home</a><span class="sep">I</span>
      <a href="#">FAQ</a><span class="sep">I</span>
      <a href="#">About Us</a>
    </nav>
    <p class="legal">© 2016 Corvane. All rights reserved.<span class="sep">I</span>Built By <span class="credit">Brightline Studio</span></p>
  </footer>
</div>
</body>
</html>
```